4 'Thank you' greetings cards designs

We are a small greetings card publisher and we need designs for a range of 'Thank you' greetings cards and notecards.
This project is for a total of 4 designs.
Please take a look at this board on Moodpinly, to see the kind of thing we are looking for: https://www.moodpinly.example/dorvek481/thank-you-cards/
The cards will be printed at a maximum size of 131mm x 183mm (including a 3mm bleed) so please provide 300dpi CMYK files at this size. Please ensure that any text (or elements of the design that are not part of the bleed) are at least 11mm in from each edge. Also, please note that cards do not have to have a bleed if your design doesn't require it (e.g. a plain white background).
Please provide 2 designs in 'portrait' orientation and 2 in 'landscape'.
Please provide 2 designs that just have the words 'Thank you' and then 2 designs that include your choice of these alternative messages:
Thank you so much
Thanks very much
Thank you very much
Thanks a million
Just to say thank you
A big thank you
A really big thank you
Feel free to use an exclamation mark on a couple of your designs, if you wish!
Other than the above guidelines, everything else is up to you in terms of colours, fonts, shapes, etc. - but please use the Moodpinly board to see the kind of designs we are looking for.
Thank you!

```html
<!DOCTYPE html>
<html lang="en">
<head>
<meta charset="utf-8">
<title>Thank You Card</title>
<link rel="stylesheet" href="https://fonts.googleapis.com/css2?family=Bebas+Neue&display=swap">
<style>
  :root {
    --paper: #ffffff;
    --ink: #060807;
    --flame: #e8380a;
  }
  html, body {
    margin: 0;
    padding: 0;
    width: 859px;
    height: 1200px;
    overflow: hidden;
    background: var(--paper);
  }
  .card {
    display: block;
    width: 859px;
    height: 1200px;
  }
  .stripe, .stripe-over { fill: var(--ink); }
  .frame { fill: none; stroke: var(--flame); stroke-width: 33; }
  .greeting {
    font-family: "Bebas Neue", "Oswald", sans-serif;
    fill: var(--flame);
  }
</style>
</head>
<body>
<svg class="card" viewBox="0 0 859 1200" xmlns="http://www.w3.org/2000/svg">
  <title>Thank you</title>
  <rect width="859" height="1200" fill="var(--paper)"/>

  <g class="stripes">
    <rect class="stripe" x="0" y="33" width="859" height="90"/>
    <rect class="stripe" x="0" y="197" width="859" height="89"/>
    <rect class="stripe" x="0" y="388" width="859" height="89"/>
    <rect class="stripe" x="0" y="579" width="859" height="89"/>
    <rect class="stripe" x="0" y="771" width="859" height="89"/>
    <rect class="stripe" x="0" y="934" width="859" height="89"/>
    <rect class="stripe" x="0" y="1075" width="859" height="90"/>
  </g>

  <rect class="frame" x="80.5" y="145.5" width="709" height="784"/>

  <g class="frame-weave">
    <rect class="stripe-over" x="60" y="386" width="41" height="93"/>
    <rect class="stripe-over" x="60" y="771" width="41" height="89"/>
    <rect class="stripe-over" x="769" y="197" width="41" height="86"/>
    <rect class="stripe-over" x="769" y="579" width="41" height="89"/>
  </g>

  <text class="greeting" x="137" y="508" font-size="316" textLength="598" lengthAdjust="spacingAndGlyphs">THANK</text>
  <text class="greeting" x="257" y="790" font-size="324" textLength="350" lengthAdjust="spacingAndGlyphs">YOU</text>

  <g class="text-weave">
    <rect class="stripe-over" x="287" y="388" width="250" height="89"/>
    <rect class="stripe-over" x="575" y="579" width="40" height="89"/>
  </g>
</svg>
</body>
</html>
```